Professional Corporate Business Card and Stationery Design for Freight Trucking Transportation Co.
Peter R. Malloy General Manager
Professional Corporate Business Card and Stationery Design for Freight Trucking Transportation Co. - Transportation
Creative Brief
Professional
Peter R. Malloy
V.P. of Operations / General Manager
7-48213 Upper Greyling Ridge Road Abbotsford, B.C. V2K4N7 Canada
HarrowTrans@pelvane.ca
This design project is for Business Cards and Business Stationey Harrow Transportation and Logistics Ltd. is a professional freight truck transport carrier based out of British Columbia, Canada. We provide highly crafted cargo delivery platforms to premier shippers of commodities throughout the five border Provinces of Canada and the Lower 48 United States of America. We are a "For-Hire" Motor Carrier which hauls shipper commodities from points within Canada to points within Canada and to points in the USA. We also transport freight from the United States into points within Canada. Threfore, we pride ourselves on superior performance and service, second to none in trucking freight industry. The above link will take you to what we feel is a example set of very highly crafted, upscale imagery designs created by artists on this very site and exemplifies the grit and character of true, quality Business card and Stationery designs, representation of the values of business professionalism we stand for and wish to convey in our stationery and other designs. Are you challenged enough to join in the fray and craft a unique design which can stand on par with those on this link? Today is April 25, 2014 - The challenge is to wow not only Harrow, but yourselves and your peers... ??
Harrow Harrow

```html
<!DOCTYPE html>
<html lang="en">
<head>
<meta charset="utf-8">
<title>Harrow Transportation and Logistics Ltd. – Business Card</title>
<link href="https://fonts.googleapis.com/css2?family=Open+Sans:wght@400;600;700&display=swap" rel="stylesheet">
<style>
  :root {
    --bg: #d9d6d3;
    --card-black: #1c1c1d;
    --brand-red: #e8222a;
    --panel-white: #ffffff;
    --panel-grey: #c9c9c9;
    --text-light: #f2f2f2;
    --text-muted: #bdbdbd;
  }
  * { margin: 0; padding: 0; box-sizing: border-box; }
  html, body { width: 1200px; height: 803px; overflow: hidden; }
  body {
    background: var(--bg);
    font-family: "Open Sans", Arial, sans-serif;
    position: relative;
  }
  .card {
    position: absolute;
    top: 250px;
    width: 520px;
    height: 300px;
    overflow: hidden;
    box-shadow: 0 10px 24px rgba(0,0,0,0.22);
  }
  .card--front { left: 50px; }
  .card--back { left: 630px; }
  .card__art { position: absolute; inset: 0; }

  .brand {
    position: absolute;
    left: 250px; top: 108px;
    display: flex; align-items: center; gap: 10px;
  }
  .brand__dot {
    width: 26px; height: 26px; border-radius: 50%;
    background: var(--brand-red);
  }
  .brand__name {
    font-weight: 700; font-size: 30px; letter-spacing: 2px;
    color: var(--brand-red);
  }
  .website {
    position: absolute;
    left: 255px; top: 172px; width: 235px;
    font-size: 14px; color: var(--panel-white); text-align: center;
  }
  .contact {
    position: absolute;
    left: 22px; top: 200px;
    color: var(--text-light); font-size: 12px; line-height: 17px;
  }
  .contact__row { display: flex; align-items: flex-start; gap: 10px; margin-bottom: 8px; }
  .contact__row svg { flex: none; margin-top: 2px; }
  .email {
    position: absolute;
    left: 300px; top: 250px;
    display: flex; align-items: center; gap: 12px;
    color: var(--text-light); font-size: 13px;
  }
  .holder {
    position: absolute;
    right: 28px; top: 30px; text-align: right;
    color: var(--text-light);
  }
  .holder__name { font-size: 19px; font-weight: 600; letter-spacing: 1.5px; text-transform: uppercase; }
  .holder__title { font-size: 12px; color: var(--text-muted); margin-top: 2px; }
</style>
</head>
<body>

  <section class="card card--front" aria-label="Business card front">
    <svg class="card__art" viewBox="0 0 520 300" width="520" height="300">
      <rect width="520" height="300" fill="var(--card-black)"/>
      <rect width="520" height="36" fill="var(--brand-red)"/>
      <path d="M0 30 H520 V214 Q520 226 508 226 H236 Q222 226 222 212 V168 Q222 150 204 150 H0 Z" fill="var(--panel-grey)"/>
      <path d="M0 26 H520 V206 Q520 216 510 216 H242 Q232 216 232 206 V160 Q232 140 212 140 H0 Z" fill="var(--panel-white)"/>
      <rect x="246" y="164" width="256" height="34" rx="17" fill="var(--brand-red)"/>
    </svg>
    <div class="brand"><span class="brand__dot"></span><span class="brand__name">HARROW</span></div>
    <div class="website">www.harrowtrans.ca</div>
    <div class="contact">
      <div class="contact__row">
        <svg width="14" height="14" viewBox="0 0 24 24"><path fill="#f2f2f2" d="M6.6 10.8a15 15 0 0 0 6.6 6.6l2.2-2.2c.3-.3.7-.4 1-.2 1.1.4 2.3.6 3.6.6.6 0 1 .4 1 1V20c0 .6-.4 1-1 1A17 17 0 0 1 3 4c0-.6.4-1 1-1h3.5c.6 0 1 .4 1 1 0 1.3.2 2.5.6 3.6.1.3 0 .7-.2 1z"/></svg>
        <span>012 555 0147<br>012 555 0147</span>
      </div>
      <div class="contact__row">
        <svg width="14" height="14" viewBox="0 0 24 24"><path fill="#f2f2f2" d="M12 3 2 12h3v8h5v-6h4v6h5v-8h3z"/></svg>
        <span>214 Ridge Plaza,<br>Harbour Road BC</span>
      </div>
    </div>
    <div class="email">
      <svg width="20" height="14" viewBox="0 0 20 14"><rect x="0.75" y="0.75" width="18.5" height="12.5" fill="none" stroke="#f2f2f2" stroke-width="1.5"/><path d="M1 1 10 8 19 1" fill="none" stroke="#f2f2f2" stroke-width="1.5"/></svg>
      <span>HarrowTrans@pelvane.ca</span>
    </div>
  </section>

  <section class="card card--back" aria-label="Business card back">
    <svg class="card__art" viewBox="0 0 520 300" width="520" height="300">
      <rect width="520" height="300" fill="var(--card-black)"/>
      <path d="M0 110 H150 Q175 110 190 130 L220 170 Q235 190 260 190 H520 V300 H0 Z" fill="var(--brand-red)"/>
      <path d="M0 130 H140 Q162 130 176 150 L204 190 Q218 210 242 210 H520 V250 H0 Z" fill="var(--panel-grey)"/>
      <path d="M0 138 H136 Q156 138 170 158 L198 198 Q211 216 234 216 H520 V242 H0 Z" fill="var(--panel-white)"/>
      <rect y="270" width="520" height="30" fill="var(--card-black)"/>
    </svg>
    <div class="holder">
      <div class="holder__name">Peter R. Malloy</div>
      <div class="holder__title">Managing Director</div>
    </div>
  </section>

</body>
</html>
```